Larkfield Meadow Apiary Co.

Using the logo created by your designer I need to have a label made for retail sales of my product (Local Raw Honey) local and raw are the key phrases that would need to stand out to the consumer on the grocery shelves or farmers markets and that this is a 100% pure product. The label will also need to include Net weight in pounds and kg with space for me to write in the numerals as I have multiple size jars (I've included my home made label for reference on the Net weight requirements for my state) and I will need my business name and address "Larkfeld Meadow Apiary Co. 1837 Tallow Creek Rd SW South Boardman Mi. 38514" at the bottom of the of the label.

```html
<!DOCTYPE html>
<html lang="en">
<head>
<meta charset="utf-8">
<title>Larkfield Meadow Apiary Co. — Jar Label</title>
<link rel="stylesheet" href="https://fonts.googleapis.com/css2?family=Jost:wght@400;500;600&display=swap">
<style>
  :root {
    --backdrop: #e6e6e6;
    --label-paper: #ffffff;
    --mark-tint: #e8e6dc;
    --brand-gold: #b48a4e;
    --ink: #2e2e2e;
    --ink-soft: #3a3a3a;
  }
  * { box-sizing: border-box; margin: 0; padding: 0; }
  html, body {
    width: 1200px;
    height: 867px;
    overflow: hidden;
    background: var(--backdrop);
  }
  .canvas {
    width: 1200px;
    height: 867px;
    display: flex;
    align-items: center;
    justify-content: center;
  }
  .jar-label {
    width: 560px;
    height: 580px;
    background: var(--label-paper);
    display: flex;
    flex-direction: column;
    align-items: center;
    padding-top: 34px;
    font-family: "Jost", sans-serif;
    box-shadow: 0 2px 10px rgba(0,0,0,0.08);
  }
  .brand-circle {
    width: 130px;
    height: 130px;
    border-radius: 50%;
    background: var(--mark-tint);
  }
  .brand-name {
    margin-top: 18px;
    font-weight: 500;
    font-size: 30px;
    line-height: 38px;
    color: var(--brand-gold);
    letter-spacing: 0.5px;
  }
  .claim-band {
    margin-top: 16px;
    width: 380px;
    text-align: center;
    border-top: 2px solid var(--ink);
    border-bottom: 2px solid var(--ink);
    padding: 4px 0 3px;
  }
  .claim-band__text {
    font-weight: 600;
    font-size: 27px;
    line-height: 34px;
    letter-spacing: 3px;
    color: var(--ink);
  }
  .purity-line {
    margin-top: 10px;
    font-weight: 500;
    font-size: 19px;
    letter-spacing: 2.4px;
    color: var(--ink);
  }
  .product-facts {
    margin-top: 18px;
    text-align: center;
    color: var(--ink-soft);
    font-weight: 500;
    font-size: 16px;
    letter-spacing: 1.8px;
    line-height: 30px;
  }
  .write-in {
    display: inline-block;
    width: 58px;
    border-bottom: 1.5px solid var(--ink-soft);
    height: 18px;
    vertical-align: baseline;
    margin: 0 4px;
  }
  .maker-address {
    margin-top: 20px;
    text-align: center;
    font-weight: 400;
    font-size: 13.5px;
    letter-spacing: 1.2px;
    line-height: 21px;
    color: var(--ink-soft);
  }
</style>
</head>
<body>
  <main class="canvas">
    <section class="jar-label">
      <div class="brand-circle" aria-hidden="true"></div>
      <h1 class="brand-name">Larkfield Meadow Apiary Co.</h1>
      <div class="claim-band">
        <p class="claim-band__text">LOCAL RAW HONEY</p>
      </div>
      <p class="purity-line">100% PURE HONEY</p>
      <div class="product-facts">
        <p>NO PRESERVATIVES</p>
        <p>NET WT <span class="write-in"></span> lb (<span class="write-in"></span> kg)</p>
      </div>
      <address class="maker-address" style="font-style: normal;">
        <p>Larkfeld Meadow Apiary Co.</p>
        <p>1837 Tallow Creek Rd SW, South Boardman Mi. 38514</p>
      </address>
    </section>
  </main>
</body>
</html>
```